Company Profile
Korvane Cargo Sdn Bhd is a well-established and experienced freight forwarder in Kuala Lumpur, Malaysia. We specialize in air and sea forwarding, Custom Brokerage and regulatory compliance services, inland transportation, overseas freighting and warehousing and distribution management. With our dedicated qualified and experienced professionals, we are fully committed to serving our clients.

Our Mission
Based on the motto “Quick, Reliable and Polite”, Korvane Cargo is dedicated to upholding the following three points corporate philosophy:1. Adhering to the principle that “the customer always comes first”.2. Contributing to the development of the local community.3. Making it our duty to be responsible and sincere.

Our Edge
• One-Stop Logistics Solutions
• Extensive Network Throughout Malaysia
• Highly Qualified and Experienced Pool of Professionals
• Comprehensive IT Solutions
• Innovative and Customer-focused Solutions
• Flexible and Consistent in Managing Exceptions
• Total Supply Chain Visibility

Target Market : We sell the logistics services to all the industry in Malaysia. (One Stop Logistics Solutions)

Business Card Detail : I would like to see the logo on the front with the general info.

Must Haves :
1) Name, Title, Office, Cell, Fax, Email, Address, Website
2) Must have complete company name show as : Korvane Cargo Sdn Bhd
3) Must have company registration no, show as : 8571620-W

Nice to Haves : Modern Design Business Card

Target Market(s)

We sell the logistics services to all the industry in Malaysia. (One Stop Logistics Solutions)

Contact Information for Business Card

I would like to see the logo on the front with the general info.

Colors

Designer to choose colors to be used in the design.

Requirements
Must have
• 1) Name, Title, Office, Cell, Fax, Email, Address, Website
• 2) Must have complete company name show as : Korvane Cargo Sdn Bhd
• 3) Must have company registration no, show as : 8571620-W
Nice to have
• Modern Design Business Card
Should not have
• Nil

```html
<!DOCTYPE html>
<html lang="en">
<head>
<meta charset="utf-8">
<title>Korvane Cargo – Business Card</title>
<link href="https://fonts.googleapis.com/css2?family=Roboto:wght@400;500;700&display=swap" rel="stylesheet">
<style>
  :root{
    --navy:#0d4f8f;
    --navy-dark:#0a4684;
    --navy-light:#1167b4;
    --sky:#29a3df;
    --ink:#3a3a3a;
    --rule:#4a4a4a;
    --white:#ffffff;
    --canvas:#e4e4e4;
  }
  *{margin:0;padding:0;box-sizing:border-box}
  html,body{width:1125px;height:1200px;overflow:hidden}
  body{background:var(--canvas);font-family:"Roboto",Arial,sans-serif;position:relative}

  .card{position:absolute;left:171px;width:826px;height:472px;border-radius:22px;overflow:hidden}

  /* front */
  .card--front{top:106px;background:var(--white)}
  .reg-no{position:absolute;left:39px;top:34px;font-size:18px;color:var(--ink)}
  .brand{position:absolute;right:40px;top:58px;display:flex;align-items:center;gap:16px}
  .brand__dot{width:64px;height:64px;border-radius:50%;background:var(--navy)}
  .brand__name{font-size:36px;font-weight:700;color:var(--navy);line-height:1;letter-spacing:1px}
  .person{position:absolute;left:39px;top:200px}
  .person__name{font-size:30px;font-weight:700;color:var(--navy);line-height:1}
  .person__title{font-size:20px;color:var(--sky);margin-top:6px}
  .divider{position:absolute;left:39px;right:40px;top:276px;height:1px;background:var(--rule)}
  .contacts{position:absolute;left:39px;top:302px;list-style:none}
  .contacts li{display:flex;align-items:center;gap:13px;font-size:19.5px;color:var(--ink);height:26.3px}
  .contacts svg{width:18px;height:18px;fill:var(--navy);flex:none}
  .address{position:absolute;right:40px;top:306px;text-align:right;font-size:19.5px;color:var(--ink);line-height:25px;font-style:normal}
  .address__company{font-weight:500}
  .band{position:absolute;left:0;right:0;bottom:0;height:12px;background:var(--sky)}

  /* back */
  .card--back{top:639px;background:linear-gradient(120deg,var(--navy-dark) 0%,var(--navy) 55%,var(--navy-light) 100%)}
  .back__brand{position:absolute;right:46px;top:318px;text-align:right;color:var(--white)}
  .back__name{font-size:40px;font-weight:700;line-height:1.05;letter-spacing:2px}
  .back__tagline{font-size:20px;margin-top:8px}
</style>
</head>
<body>

<section class="card card--front" aria-label="Business card front">
  <p class="reg-no">Reg No: 8571620-W</p>

  <div class="brand">
    <span class="brand__dot"></span>
    <span class="brand__name">KORVANE CARGO</span>
  </div>

  <div class="person">
    <h1 class="person__name">DANIEL TAN</h1>
    <p class="person__title">Managing Director</p>
  </div>

  <div class="divider"></div>

  <ul class="contacts">
    <li><svg viewBox="0 0 24 24"><path d="M6.6 10.8a15.1 15.1 0 0 0 6.6 6.6l2.2-2.2a1 1 0 0 1 1-.25 11.4 11.4 0 0 0 3.6.57 1 1 0 0 1 1 1V20a1 1 0 0 1-1 1A17 17 0 0 1 3 4a1 1 0 0 1 1-1h3.5a1 1 0 0 1 1 1c0 1.25.2 2.45.57 3.57a1 1 0 0 1-.25 1z"/></svg>(+603) 3327 5810 / 5811</li>
    <li><svg viewBox="0 0 24 24"><path d="M7 1h10a2 2 0 0 1 2 2v18a2 2 0 0 1-2 2H7a2 2 0 0 1-2-2V3a2 2 0 0 1 2-2zm0 3v14h10V4z"/></svg>(+6012) 648 2093</li>
    <li><svg viewBox="0 0 24 24"><path d="M6 2h9l3 3v5H6zM3 11h18a1 1 0 0 1 1 1v9H2v-9a1 1 0 0 1 1-1zm3 4v2h12v-2z"/></svg>(+603) 3327 5812</li>
    <li><svg viewBox="0 0 24 24"><path d="M2 5h20v14H2zm2 2v.5l8 5 8-5V7l-8 5z"/></svg>daniel.tan@korvanecargo.com.my</li>
    <li><svg viewBox="0 0 24 24"><path d="M12 2a10 10 0 1 0 0 20 10 10 0 0 0 0-20zm-1 17.9A8 8 0 0 1 4.2 10.2L9 15v1a2 2 0 0 0 2 2zm6.9-2.5A2 2 0 0 0 16 16h-1v-3a1 1 0 0 0-1-1H8v-2h2a1 1 0 0 0 1-1V7h2a2 2 0 0 0 2-2v-.4a8 8 0 0 1 2.9 12.8z"/></svg>www.korvanecargo.com.my</li>
  </ul>

  <address class="address">
    <span class="address__company">Korvane Cargo Sdn Bhd</span><br>
    No.22B, 2nd Floor<br>
    Jalan Seri Permai 3/KS4<br>
    Taman Seri Permai, 41150 Klang<br>
    Selangor Darul Ehsan, Malaysia
  </address>

  <div class="band"></div>
</section>

<section class="card card--back" aria-label="Business card back">
  <div class="back__brand">
    <p class="back__name">KORVANE<br>CARGO</p>
    <p class="back__tagline">One Stop Logistics Specialist</p>
  </div>
</section>

</body>
</html>
```